Marlow Sips, alcoholic beverages with real fruit - Can Redesign

Background

Marlow Sips is a Sydney-based beverage company crafted by three long time mates. The trio decided to develop their own range of tasty, healthy alternative premix alcohol options, after seeing a huge gap in the market.

Our difference? Our beverages are crafted with premium real fruit purees that deliver unreal taste.

See website: www.marlowsips-example.com
See instagram: marlow.sips

Marlow currently has 2 flavours in store - both of which have been super successful after just 5 months on shelf. The flavours:

Vodka soda lime
A mouth-watering take on an Aussie staple. Packed full of real limes (skin and all, to eliminate waste) delivering a refreshing, zesty flavour. A splash of apple juice provides natural sweetness and well rounded mouthfeel.

A highly sessionable vodka soda lime with unreal taste! Best served cold with mates.

Gin soda cucumber
The perfect combo? Our gin soda cucumber tastes just like your favourite bartender made it. Crafted with real, whole, pureed cucumbers for a refreshing, clean flavour. Balanced flawlessly with a gin featuring juniper, coriander, lemon peel, cardamom and so much more.

What is required

This brief is for the design refresh of our 2 cans.

Since launching in 2020, we have come to realise our original can designs could use a bit of an update. To customers passing by in the store, it may not be immediately obvious exactly what Marlow is. Some recent feedback on the cans included:

A customer needs to know what the product is right away when looking into fully stocked RTD/Seltzer fridges in store. The Marlow can doesn’t currently do this.
When customers glance at the can, they should be able to immediately know what the drink is, what flavour the drink is and potentially a specific USP that will make them pick up this can, over any other.

The primary objective of the can design is to get customers’ attention through hero-ing the flavour of each can on the front/side through the use of text, colour or imagery.

The specifics

The key new points that must be included on the updated can design are:

Highlight the fact our drinks use REAL FRUIT (real lime - the whole thing, and real cucumber).
This is our key USP and is why our beverages are so tasty compared to anything in stores. We want to bring this to life on our cans.
Bring to life the key flavour of each (Lime on the vodka can, Cucumber on the gin can). This could be through colour, text or imagery.
Currently, the text size and location of each flavour is quite small. And other than this text, there is no other reference to the key flavour on the can designs.

What can stay the same:

Please keep the Buff colour scheme for the vodka, and the Blue colour scheme for the gin can.
PLEASE NOTE: do not use more than 6 different colours. You pay per colour when setting up print on cans.

Please keep the MARLOW logo prominent on the front of the can. Position and sizing can change.

The Marlow infographic (3 stick figures) around the neck of the can to please remain.

USPS to remain the same - the position and sizing can change:

All natural
89 calories
Low sugar

What can change:
Location of instagram handle is flexible
Infographics (Kooly / Record Player) are open to interpretation. They can be kept, modified, removed or replaced.
All babydoll text to increase in size.

Please see our brand Tone of Voice and Guidelines. PLEASE NOTE the design needs to remain in our identity which can be seen on our website and instagram. We do not want a corporate style; it needs to be unique.

Files Provided:

Link to all required files: https://files.quillbox-example.net/receive/TrOpelanvx?ref=QxBZ7mKdLwRf2NsPv8HjTcYe3UaGk

Target Market(s)

Males and females aged 18-40. Social, affluent, health conscious, supports local businesses, taste driven, enjoys trying new products

Font styles to use
Other font styles liked:
• Baby doll and Futura

Requirements
Must have
• A customer needs to know what the product is right away when looking into fully stocked RTD/Seltzer fridges in store. The Marlow can doesn’t currently do this.

All natural
89 calories
Low sugar
Nice to have
• A concept we are keen to explore is having the look of ripped/torn paper with the flavour exposed (e.g. green colour) underneath, see "torn paper examples" attachment for rough examples. This could be done in an illustrative style using black and buff lines on the respective cans. If this doesn't fit with your style please feel free to ignore this concept.
Should not have
• Alcohol marketing standards in Australia prevent any of the following:

show, directly imply or encourage excessive or rapid consumption of alcohol, misuse or abuse of alcohol or consumption inconsistent with the National Beverage Code

show, directly imply or encourage irresponsible or offensive alcohol related behaviour

challenge or dare people to consume an alcohol beverage

encourage choice of an alcohol beverage by emphasising its alcohol strength/intoxicating effect

have strong or evident appeal to minors

show under 25 year olds (or over 25 year olds that look like they are under 18 years of age)

suggest the consumption/presence of alcohol could contribute to a significant change in mood or environment

show or directly imply the consumption or presence of alcohol as leading to personal, business, social, sporting, sexual or other success

Imply/suggest that alcohol shown as part of a celebration is a cause of the success/ achievement

suggest the consumption of alcohol offers a therapeutic benefit or is a necessary aid to relaxation

show or directly imply the consumption of alcohol before or during any activity that for safety reasons

requires you to be alert or physically co-ordinated (i.e. driving or swimming)

```html
<!DOCTYPE html>
<html lang="en">
<head>
<meta charset="utf-8">
<title>Marlow Sips – Can Redesign</title>
<link rel="stylesheet" href="https://fonts.googleapis.com/css2?family=Gochi+Hand&family=Patrick+Hand&display=swap">
<style>
  :root {
    --backdrop: #fbe0cc;
    --buff: #e3cab5;
    --blue: #465166;
    --ink: #2b2a29;
    --rim: #d8d8d6;
    --rim-shade: #b9b9b7;
    --lime-deep: #4f8f2c;
    --lime-type: #c4eb86;
    --lime-note: #3c7a1e;
    --cucumber-deep: #2a5e2a;
    --cucumber-type: #a9dc8e;
    --peel: #f1f1ef;
  }
  * { margin: 0; padding: 0; box-sizing: border-box; }
  html, body { width: 1200px; height: 777px; overflow: hidden; }
  body { background: var(--backdrop); position: relative; font-family: "Patrick Hand", cursive; }

  .can { position: absolute; top: 55px; width: 382px; height: 675px; }
  .can--vodka { left: 153px; --body: var(--buff); --mark: var(--ink); }
  .can--gin { left: 687px; --body: var(--blue); --mark: var(--buff); }

  .can__lid, .can__base {
    position: absolute; left: 34px; right: 34px; height: 26px;
    background: linear-gradient(90deg, var(--rim-shade), var(--rim), var(--rim-shade));
  }
  .can__lid { top: 0; border-radius: 12px 12px 4px 4px; }
  .can__base { bottom: 0; border-radius: 4px 4px 18px 18px; }
  .can__body {
    position: absolute; top: 22px; bottom: 22px; left: 0; right: 0;
    background: var(--body); border-radius: 28px;
  }

  .handle {
    position: absolute; top: 108px; width: 100%; text-align: center;
    font-size: 17px; letter-spacing: 0.5px; color: var(--mark);
  }
  .figures {
    position: absolute; top: 244px; left: 50%; transform: translateX(-50%);
    width: 58px; height: 22px; border-radius: 4px; opacity: 0.3;
    background: var(--mark);
  }
  .wordmark {
    position: absolute; top: 266px; width: 100%; text-align: center;
    font-size: 64px; font-weight: 400; letter-spacing: 5px; line-height: 1; color: var(--mark);
  }
  .wordmark-rule {
    position: absolute; top: 342px; left: 50%; transform: translateX(-50%);
    width: 224px; height: 5px; border-radius: 3px; background: var(--mark);
  }

  .flavour { position: absolute; left: 71px; top: 387px; width: 232px; height: 202px; }
  .flavour svg { display: block; width: 100%; height: 100%; }
  .flavour text { font-family: "Gochi Hand", cursive; }
</style>
</head>
<body>

<section class="can can--vodka" aria-label="Marlow vodka soda lime can">
  <div class="can__lid"></div>
  <div class="can__body">
    <p class="handle">@marlow.sips</p>
    <div class="figures" role="img" aria-label="Three stick figures above the Marlow name"></div>
    <h1 class="wordmark">MARLOW</h1>
    <div class="wordmark-rule"></div>
    <div class="flavour">
      <svg viewBox="0 0 232 202">
        <defs>
          <linearGradient id="lime-fill" x1="0" y1="1" x2="1" y2="0">
            <stop offset="0.42" stop-color="var(--peel)"/>
            <stop offset="0.6" stop-color="var(--lime-deep)"/>
          </linearGradient>
        </defs>
        <rect width="232" height="202" rx="8" fill="url(#lime-fill)" role="img"
              aria-label="Illustration of a peeling label revealing lime green beneath"/>
        <text x="110" y="50" transform="rotate(55 110 50)" font-size="32" fill="var(--lime-type)">LIME</text>
        <text x="150" y="130" font-size="12" fill="var(--lime-note)">real lime</text>
        <text x="10" y="100" transform="rotate(35 10 100)" font-size="24" fill="var(--ink)">VODKA +</text>
        <text x="4" y="134" transform="rotate(35 4 134)" font-size="24" fill="var(--ink)">SODA</text>
        <text x="72" y="190" font-size="19" fill="var(--ink)">4.2%</text>
      </svg>
    </div>
  </div>
  <div class="can__base"></div>
</section>

<section class="can can--gin" aria-label="Marlow gin soda cucumber can">
  <div class="can__lid"></div>
  <div class="can__body">
    <p class="handle">@marlow.sips</p>
    <div class="figures" role="img" aria-label="Three stick figures above the Marlow name"></div>
    <h2 class="wordmark">MARLOW</h2>
    <div class="wordmark-rule"></div>
    <div class="flavour">
      <svg viewBox="0 0 232 202">
        <defs>
          <linearGradient id="cucumber-fill" x1="0" y1="1" x2="1" y2="0">
            <stop offset="0.42" stop-color="var(--peel)"/>
            <stop offset="0.6" stop-color="var(--cucumber-deep)"/>
          </linearGradient>
        </defs>
        <rect width="232" height="202" rx="8" fill="url(#cucumber-fill)" role="img"
              aria-label="Illustration of a peeling label revealing cucumber green beneath"/>
        <text x="62" y="38" transform="rotate(45 62 38)" font-size="28" fill="var(--cucumber-type)">CUCUMBER</text>
        <text x="14" y="104" transform="rotate(35 14 104)" font-size="24" fill="var(--blue)">GIN +</text>
        <text x="6" y="136" transform="rotate(35 6 136)" font-size="24" fill="var(--blue)">SODA</text>
        <text x="74" y="190" font-size="19" fill="var(--blue)">4.2%</text>
      </svg>
    </div>
  </div>
  <div class="can__base"></div>
</section>

</body>
</html>
```